Brindle Deals is an online marketing platform

A daily deals site for consumers a way to bring in new clients for clients and this is who the business cards are for. Industries - Food and Drink, Things To Do, Beauty and Spas, Staycations and Services.This leaflet is going to be used to get member of the public to sign up to our website

```html
<!DOCTYPE html>
<html lang="en">
<head>
<meta charset="utf-8">
<title>Brindle Deals – Launch Leaflet</title>
<link rel="stylesheet" href="https://fonts.googleapis.com/css2?family=Dancing+Script:wght@600;700&family=Kaushan+Script&family=Tinos:wght@400;700&display=swap">
<style>
  :root {
    --backdrop: #d6d6d6;
    --paper: #ffffff;
    --brand-blue: #0d4ea6;
    --ink: #1e1e1e;
    --band: #0c0c0c;
    --band-text: #ffffff;
    --accent-yellow: #f6ef8e;
  }
  * { box-sizing: border-box; margin: 0; padding: 0; }
  html, body { width: 1200px; height: 1200px; overflow: hidden; }
  body { background: var(--backdrop); position: relative; font-family: "Tinos", "Times New Roman", serif; }

  .leaflet {
    position: absolute; left: 220px; top: 62px;
    width: 760px; height: 1076px;
    background: var(--paper); overflow: hidden;
  }

  .hex-gallery { position: absolute; left: 0; top: 0; width: 760px; height: 400px; display: block; }

  .brand {
    position: absolute; left: 470px; top: 36px; width: 270px;
    display: flex; align-items: center; gap: 10px;
  }
  .brand__dot { width: 34px; height: 34px; border-radius: 50%; background: var(--brand-blue); flex: none; }
  .brand__name { font-weight: 700; font-size: 38px; color: var(--brand-blue); line-height: 1; white-space: nowrap; }

  .headline {
    position: absolute; left: 0; right: 0; top: 404px;
    text-align: center; font-family: "Dancing Script", cursive;
    font-weight: 700; font-size: 34px; line-height: 40px; color: var(--brand-blue);
  }
  .intro {
    position: absolute; left: 0; right: 0; top: 500px;
    text-align: center; font-size: 14.5px; line-height: 21px; color: var(--ink);
  }
  .tease {
    position: absolute; left: 0; right: 0; top: 551px;
    text-align: center; font-family: "Kaushan Script", cursive;
    font-size: 54px; line-height: 80px; color: var(--brand-blue);
  }
  .launch-pill {
    position: absolute; left: 129px; top: 643px; width: 498px; height: 71px;
    background: var(--brand-blue); border-radius: 18px;
    color: #fff; text-align: center; font-size: 19px; line-height: 25px;
    padding-top: 10px;
    box-shadow: 0 7px 6px -3px rgba(0,0,0,0.35);
  }
  .launch-pill sup { font-size: 9px; }
  .register {
    position: absolute; left: 0; right: 0; top: 730px;
    text-align: center; font-size: 18px; line-height: 28px; color: var(--ink);
  }
  .register strong { color: var(--brand-blue); }

  .signup-band {
    position: absolute; left: 0; top: 806px; width: 760px; height: 270px;
    background: var(--band); color: var(--band-text);
    border-top: 2px dotted #555;
  }
  .signup-band__intro {
    position: absolute; left: 41px; top: 24px; width: 680px;
    font-weight: 700; font-size: 16.5px; line-height: 20px; letter-spacing: 0.5px;
  }
  .signup-form { position: absolute; left: 41px; top: 76px; width: 400px; }
  .signup-form__field { display: flex; align-items: flex-end; height: 30px; }
  .signup-form__label { width: 94px; font-weight: 700; font-size: 19.5px; line-height: 1; }
  .signup-form__line { width: 289px; border-bottom: 1px solid #fff; margin-bottom: 3px; }
  .signup-band__optout {
    position: absolute; left: 41px; top: 209px; width: 460px;
    font-size: 14px; line-height: 17px;
  }
  .follow {
    position: absolute; left: 548px; top: 102px; width: 160px; text-align: center;
  }
  .follow__title { font-size: 34px; color: var(--accent-yellow); line-height: 40px; }
  .follow__icons { display: flex; justify-content: center; gap: 38px; margin-top: 17px; }
  .follow__icon { width: 47px; height: 47px; border-radius: 50%; background: var(--accent-yellow); }
</style>
</head>
<body>
<main class="leaflet">

  <svg class="hex-gallery" viewBox="0 0 760 400" role="img" aria-label="Photo collage in hexagons: friends smiling and sharing food and wine at an outdoor table">
    <defs>
      <linearGradient id="dineTone" x1="0" y1="0" x2="1" y2="1">
        <stop offset="0" stop-color="#9fae86"/>
        <stop offset="0.45" stop-color="#d9b79e"/>
        <stop offset="1" stop-color="#f1ece6"/>
      </linearGradient>
    </defs>
    <g fill="url(#dineTone)" stroke="#fff" stroke-width="4">
      <polygon points="73,-13 142,27 142,107 73,147 4,107 4,27"/>
      <polygon points="212,-13 281,27 281,107 212,147 143,107 143,27"/>
      <polygon points="351,-13 420,27 420,107 351,147 282,107 282,27"/>
      <polygon points="3,107 72,147 72,227 3,267 -66,227 -66,147"/>
      <polygon points="142,107 211,147 211,227 142,267 73,227 73,147"/>
      <polygon points="282,107 351,147 351,227 282,267 213,227 213,147"/>
      <polygon points="421,107 490,147 490,227 421,267 352,227 352,147"/>
      <polygon points="73,232 142,272 142,352 73,392 4,352 4,272"/>
      <polygon points="212,232 281,272 281,352 212,392 143,352 143,272"/>
      <polygon points="351,232 420,272 420,352 351,392 282,352 282,272"/>
    </g>
  </svg>

  <svg class="hex-gallery" viewBox="0 0 760 400" role="img" aria-label="Photo collage in hexagons: woman relaxing with a face mask at a spa">
    <defs>
      <linearGradient id="spaTone" x1="0" y1="0" x2="1" y2="1">
        <stop offset="0" stop-color="#e8ddd2"/>
        <stop offset="0.5" stop-color="#d8b7a0"/>
        <stop offset="1" stop-color="#f4f2f0"/>
      </linearGradient>
    </defs>
    <g fill="url(#spaTone)" stroke="#fff" stroke-width="4">
      <polygon points="617,121 685,160 685,238 617,277 549,238 549,160"/>
      <polygon points="752,121 820,160 820,238 752,277 684,238 684,160"/>
      <polygon points="549,238 617,277 617,355 549,394 481,355 481,277"/>
      <polygon points="684,238 752,277 752,355 684,394 616,355 616,277"/>
    </g>
  </svg>

  <div class="brand">
    <span class="brand__dot"></span>
    <span class="brand__name">Brindle Deals</span>
  </div>

  <h1 class="headline">Hey You! Want to win £200 to spend on the best<br>experiences the South West has to offer?</h1>

  <p class="intro">Brindle Deals is a brand spanking new website that gives you access to exciting offers<br>across the best restaurants, hotels, spas, leisure activities and services.</p>

  <p class="tease">Pretty cool?</p>

  <p class="launch-pill">Launching on the <b>1<sup>st</sup> August 2019</b> – Be the first to receive<br>exclusive offers and WIN!</p>

  <p class="register">Register for free now at <strong>brindledeals.co.uk</strong> and find inspiration for places to <strong>EAT</strong>,<br>things to <strong>DO</strong> and where to get a <strong>PAMPER</strong>.</p>

  <section class="signup-band">
    <p class="signup-band__intro">Complete your details below for your chance to win and be the first to receive<br>fresh fancy offers just for you.</p>
    <div class="signup-form">
      <div class="signup-form__field"><span class="signup-form__label">Name:</span><span class="signup-form__line"></span></div>
      <div class="signup-form__field"><span class="signup-form__label">Email:</span><span class="signup-form__line"></span></div>
      <div class="signup-form__field"><span class="signup-form__label">Mobile:</span><span class="signup-form__line"></span></div>
      <div class="signup-form__field"><span class="signup-form__label">Address:</span><span class="signup-form__line"></span></div>
    </div>
    <p class="signup-band__optout">( ) Please tick here if you would not like to receive updates on<br>fabulous offers and new experiences.</p>
    <div class="follow">
      <p class="follow__title">Follow us</p>
      <div class="follow__icons">
        <span class="follow__icon"></span>
        <span class="follow__icon"></span>
      </div>
    </div>
  </section>

</main>
</body>
</html>
```